Marta Belle Designs & Events business card

I need an elegant informative but not busy business card using my logo. We are a florist with high end customers. I am adding a PDF file and a PNG file for those who requested it
Updates

Target Market(s)

Brides, grooms, men purchasing flowers
Ages 20-65

Industry/Entity Type

Florist

Requirements
Must have
• Business info:
Marta Belle Design & Events
www.martabelleevents-sample.com.
555-418-2763

555-418-2763
Nice to have
• Est 1954
may want Pinterest logo, twitter and linkedin and facbook
Should not have
• Clip art or photos

```html
<!DOCTYPE html>
<html lang="en">
<head>
<meta charset="utf-8">
<title>Marta Belle Designs &amp; Events – Business Card</title>
<link rel="stylesheet" href="https://fonts.googleapis.com/css2?family=Source+Sans+3:wght@400;600&display=swap">
<style>
  :root {
    --page: #ffffff;
    --card-center: #e6f2d9;
    --card-edge: #d4eedc;
    --card-border: #c9c9c9;
    --rule-green: #1e8a44;
    --est-green: #1f8f4a;
    --ink: #0d0d0d;
    --blush: #d89a9a;
    --petal: rgba(176, 203, 215, 0.85);
    --petal-fade: rgba(176, 203, 215, 0);
    --strip: #d6efdb;
    --social: #6a86a8;
  }
  * { margin: 0; padding: 0; box-sizing: border-box; }
  html, body {
    width: 1200px; height: 1000px; overflow: hidden;
    background: var(--page);
    font-family: "Source Sans 3", "Myriad Pro", Arial, sans-serif;
  }
  .canvas { position: relative; width: 1200px; height: 1000px; }

  .card {
    position: absolute;
    background: radial-gradient(ellipse at 50% 50%, var(--card-center) 0%, var(--card-edge) 80%);
    overflow: hidden;
  }

  /* front */
  .card-front {
    left: 188px; top: 16px; width: 780px; height: 394px;
    border: 3px solid var(--card-border);
  }
  .front-brand {
    position: absolute; left: 220px; top: 112px; width: 280px; height: 178px;
    background: #e3eed6;
    display: flex; flex-direction: column; align-items: center; justify-content: center; gap: 14px;
  }
  .brand-dot {
    width: 34px; height: 34px; border-radius: 50%;
    background: var(--blush);
  }
  .front-brand .brand-name {
    font-weight: 400; font-size: 22px; color: var(--ink);
    letter-spacing: 0.5px; text-align: center; line-height: 1.15;
  }

  /* back */
  .card-strip {
    position: absolute; left: 960px; top: 429px; width: 25px; height: 403px;
    background: var(--strip);
  }
  .card-back {
    left: 188px; top: 427px; width: 774px; height: 402px;
    border: 3px solid var(--card-border); border-right: none;
  }
  .rule { position: absolute; left: 0; right: 0; height: 3px; background: var(--rule-green); z-index: 2; }
  .rule-top { top: 0; }
  .rule-bottom { bottom: 2px; }

  .petal-area {
    position: absolute; right: 0; top: 0; width: 290px; height: 100%;
    background: radial-gradient(ellipse at 100% 50%, var(--petal) 0%, var(--petal) 35%, var(--petal-fade) 100%);
  }

  .back-brand {
    position: absolute; left: 34px; top: 42px;
    display: flex; align-items: center; gap: 10px;
  }
  .back-brand .brand-name { font-weight: 400; font-size: 20px; color: var(--ink); }

  .business-name {
    position: absolute; left: 0; width: 806px; top: 142px; text-align: center;
    font-size: 31px; font-weight: 400; color: var(--ink);
  }
  .phone {
    position: absolute; left: 0; width: 776px; top: 205px; text-align: center;
    font-size: 28px; color: var(--ink); letter-spacing: 0.5px;
  }
  .established {
    position: absolute; left: 265px; top: 306px; width: 210px;
    display: flex; align-items: center; gap: 6px;
    color: var(--est-green); font-size: 20px;
  }
  .established .line { flex: 1; height: 2px; background: var(--est-green); }
  .website {
    position: absolute; left: 0; width: 746px; top: 360px; text-align: center;
    font-size: 20px; color: var(--ink);
  }
  .social { position: absolute; left: 698px; top: 370px; display: flex; gap: 3px; }
  .social span { width: 21px; height: 21px; border-radius: 3px; background: var(--social); display: block; }
</style>
</head>
<body>
<main class="canvas">
  <section class="card card-front" aria-label="Card front">
    <div class="front-brand">
      <span class="brand-dot"></span>
      <span class="brand-name">Marta Belle<br>Designs &amp; Events</span>
    </div>
  </section>

  <div class="card-strip"></div>
  <section class="card card-back" aria-label="Card back">
    <div class="rule rule-top"></div>
    <div class="petal-area" role="img" aria-label="Soft blue flower petal illustration along the right edge"></div>

    <div class="back-brand">
      <span class="brand-dot"></span>
      <span class="brand-name">Marta Belle</span>
    </div>

    <p class="business-name">Marta Belle Design &amp; Events</p>
    <p class="phone">555-418-2763</p>
    <p class="established"><span class="line"></span>Est. 1954<span class="line"></span></p>
    <p class="website">www.martabelleevents-sample.com</p>
    <div class="social" aria-label="Social links"><span></span><span></span></div>
    <div class="rule rule-bottom"></div>
  </section>
</main>
</body>
</html>
```